Website Design - Photo Shop Design - Functional Cash Register Layout for POS System

Design a webpage for Point of Sale site. A cash register page.

Page must have a good look. I have attached a file of a possible layout example - but need a much nicer design. I have also attached the site logo. which i will upload without background tomorrow hopefully.

Looking for a nice Fresh look , not dark and dingy.

Target Market(s)

Business

Industry/Entity Type

Business Software

Number of Pages Required

1 page

Colors
f59195
f04a50
ec1f27
fbd4d5
ffffff
f8f3f8
fdf0f6
feeeee
ecf5f6

Requirements
Must have
• Cash register layout for POS software site. Nice layout ,
Nice to have
• Try putting he register part on the left side as well as the right - invert the designs have them different to the layout example shown too.
Should not have
• Not to dark

```html
<!DOCTYPE html>
<html lang="en">
<head>
<meta charset="utf-8">
<title>TillNest – Cash Register</title>
<link href="https://fonts.googleapis.com/css2?family=Raleway:wght@400;500;600;700&display=swap" rel="stylesheet">
<style>
:root{
  --red:#ec1f27;
  --red-mid:#f04a50;
  --red-soft:#f59195;
  --pink-line:#fbd4d5;
  --white:#ffffff;
  --lilac:#f8f3f8;
  --lilac-deep:#f3e9f2;
  --blush:#fdf0f6;
  --rose:#feeeee;
  --mint:#ecf5f6;
  --mint-line:#d6e6e8;
  --slate:#66676b;
  --slate-2:#6e6f73;
  --ink:#222222;
  --grey-band:#cfcfcf;
  --grey-1:#e8e8e8;
  --grey-2:#d4d4d4;
  --grey-3:#eeeeee;
  --dash:#b9c3c5;
}
*{box-sizing:border-box;margin:0;padding:0}
html,body{width:1200px;height:855px;overflow:hidden;background:var(--white)}
body{font-family:"Raleway",sans-serif;color:var(--ink)}
.stage{position:relative;width:1171px;height:834px;transform:scale(1.0248,1.0252);transform-origin:0 0}
.abs{position:absolute}
svg{display:block}

/* sidebar */
.sidebar{left:0;top:0;width:307px;height:783px;background:var(--mint)}
.brand{left:28px;top:30px;display:flex;align-items:center;gap:10px;font-size:34px;font-weight:700;color:var(--red);letter-spacing:-.5px}
.brand-dot{width:30px;height:30px;border-radius:50%;background:var(--red)}
.nav{left:10px;top:148px;width:293px;list-style:none}
.nav li{display:flex;align-items:center;height:53px;border-bottom:1px dashed var(--dash);padding-left:20px;font-size:14.5px;font-weight:500;letter-spacing:.3px;position:relative}
.nav li svg{width:28px;height:28px;margin-right:16px;stroke:var(--ink);fill:none;stroke-width:1.3}
.nav .chev{position:absolute;right:30px;width:10px;height:10px;margin:0}
.store-badge{left:38px;top:421px;width:161px;height:46px;border-radius:6px;background:#000}
.nav-refresh{top:484px}
.nav-refresh li{border-top:1px dashed var(--dash);height:60px}

/* top */
.search{left:355px;top:19px;width:485px;height:41px;background:var(--lilac);border:1px solid #e6dfe6;border-radius:2px;display:flex;align-items:center;padding:0 14px 0 21px;font-size:14.5px;letter-spacing:.6px;justify-content:space-between}
.register-btn{left:885px;top:19px;width:245px;height:28px;background:var(--red);color:var(--white);font-size:14px;letter-spacing:.4px;display:flex;align-items:center;justify-content:center}
.menu-icon{left:1143px;top:25px;width:15px;height:13px}

/* products */
.grid{left:320px;top:99px;display:grid;grid-template-columns:repeat(4,130px);gap:7px 6px}
.tile{height:143px;border:2px solid var(--pink-line);display:flex;flex-direction:column}
.tile .ico{flex:1;display:flex;align-items:center;justify-content:center}
.tile .ico svg{width:54px;height:54px;fill:none;stroke:#111;stroke-width:2.4;stroke-linecap:round;stroke-linejoin:round}
.tile .label{height:38px;background:var(--white);display:flex;align-items:center;justify-content:center;font-size:14px;white-space:nowrap;overflow:hidden}
.t-rose{background:var(--rose)}
.t-blush{background:var(--blush)}
.t-lilac{background:var(--lilac)}
.t-mint{background:var(--mint);border-color:var(--mint-line)}
.t-active{background:var(--slate);border-color:var(--slate)}
.t-active .ico svg{stroke:var(--white)}
.t-active .label{background:var(--red);color:var(--white)}
.pager{top:421px;height:31px;background:var(--mint);display:flex;align-items:center;gap:12px;font-size:14px;padding:0 12px}
.prev{left:323px;width:108px}
.next{left:747px;width:108px;justify-content:flex-end}
.pager svg{width:8px;height:10px;stroke:#111;fill:none;stroke-width:1.8}
.cats{left:320px;top:479px;width:535px;height:38px;background:var(--grey-1);display:flex;font-size:14.5px}
.cats>div{display:flex;align-items:center;justify-content:center}
.cats svg{width:9px;height:12px;stroke:#111;fill:none;stroke-width:2}
.cat-arrow{width:38px;background:#dcdcdc}
.cat-all{width:99px;background:var(--grey-2)}
.cat{width:99px;background:var(--grey-3)}
.cat-wide{width:126px}
.cat-fill{flex:1}

/* order panel */
.order{left:871px;top:98px;width:300px}
.order-head{display:flex;height:71px;color:var(--white);font-size:14.5px}
.cust{width:181px;background:var(--slate);display:flex;align-items:center;padding-left:22px;gap:10px}
.cust svg{width:18px;height:18px;stroke:var(--white);fill:none;stroke-width:1.4}
.txn{flex:1;background:var(--slate-2);text-align:right;padding:23px 14px 0 0;line-height:20px}
.order-body{display:flex;height:413px}
.lines{width:181px;background:var(--lilac);position:relative}
.side{flex:1;background:var(--lilac-deep)}
.notes{position:absolute;left:14px;bottom:25px;display:flex;align-items:center;gap:8px;font-size:14.5px}
.notes span{width:26px;height:26px;background:#e6e6e6;display:flex;align-items:center;justify-content:center;font-size:13px}
.totals{left:871px;top:592px;width:300px;text-align:center;font-size:10px;line-height:24px;font-weight:500}
.park-plus{left:910px;top:644px;width:37px;height:37px;background:#e3e3e3;display:flex;align-items:center;justify-content:center;font-size:16px}
.park{left:952px;top:644px;width:174px;height:37px;background:#e3e3e3;display:flex;align-items:center;justify-content:center;font-size:14.5px}
.pay{left:910px;top:687px;width:216px;height:37px;background:linear-gradient(90deg,var(--red),var(--red-mid));color:var(--white);font-weight:700;font-size:14px;display:flex;align-items:center;justify-content:space-between;padding:0 11px 0 22px;letter-spacing:.5px}

/* footer */
.footer{left:0;top:783px;width:1171px;height:51px;background:var(--grey-band);font-size:12.5px;display:flex;align-items:center;justify-content:space-between;padding:0 12px 0 38px;letter-spacing:.2px}
.chat{left:1056px;top:759px;width:53px;height:53px;border-radius:50%;background:#595959;display:flex;align-items:center;justify-content:center}
.chat svg{width:26px;height:24px;stroke:var(--white);fill:none;stroke-width:1.5}
</style>
</head>
<body>
<div class="stage">

  <aside class="abs sidebar">
    <div class="abs brand"><span class="brand-dot"></span>TillNest</div>
    <ul class="abs nav">
      <li><svg viewBox="0 0 28 28"><path d="M3 14 14 4l11 10M6 12v12h6v-7h4v7h6V12"/></svg>ENTER SALE</li>
      <li><svg viewBox="0 0 28 28"><path d="M9 24V4M4 9l5-5 5 5M19 4v20M14 19l5 5 5-5"/></svg>PARKED / LAYBY ORDERS</li>
      <li><svg viewBox="0 0 28 28"><path d="M14 2l3 3h5v5l3 4-3 4v5h-5l-3 3-3-3H6v-5l-3-4 3-4V5h5z"/><path d="M10 18l8-8"/><circle cx="10.5" cy="10.5" r="1.5"/><circle cx="17.5" cy="17.5" r="1.5"/></svg>COMPLETED SALES</li>
      <li><svg viewBox="0 0 28 28"><rect x="3" y="5" width="22" height="20"/><path d="M3 10h22M8 3v4M20 3v4"/><text x="8" y="22" font-size="9" fill="#222" stroke="none" font-family="sans-serif">15</text></svg>APPOINTMENTS</li>
      <li><svg viewBox="0 0 28 28"><rect x="5" y="3" width="16" height="22"/><path d="M9 8h8M9 12h8M9 16h5M21 12h3v12H13"/></svg>BACK OFFICE<svg class="chev" viewBox="0 0 10 10"><path d="M3 1l4 4-4 4"/></svg></li>
    </ul>
    <div class="abs store-badge" role="img" aria-label="App download badge"></div>
    <ul class="abs nav nav-refresh">
      <li><svg viewBox="0 0 28 28"><path d="M16 3H6v22h8M16 3l5 5v5M16 3v5h5M9 11h7M9 15h5"/><path d="M24 19a5 5 0 1 1-2-4M23 13v3h-3"/></svg>REFRESH DATA</li>
    </ul>
  </aside>

  <div class="abs search">Search Product by Name or Sku...
    <svg width="19" height="19" viewBox="0 0 20 20" fill="none" stroke="#999" stroke-width="2.6"><circle cx="8" cy="8" r="6"/><path d="M12.5 12.5 18 18"/></svg>
  </div>
  <div class="abs register-btn">MY SHOP / CASH REGISTER 1</div>
  <svg class="abs menu-icon" viewBox="0 0 15 13" fill="#111"><rect width="15" height="3"/><rect y="5" width="15" height="3"/><rect y="10" width="15" height="3"/></svg>

  <section class="abs grid">
    <div class="tile t-active"><div class="ico"><svg viewBox="0 0 54 54"><rect x="5" y="7" width="44" height="32"/><path d="M3 7h48M27 39v10M22 49h10M13 31l9-10 6 6 12-12"/></svg></div><div class="label">Demo Product</div></div>
    <div class="tile t-rose"><div class="ico"><svg viewBox="0 0 54 54"><circle cx="24" cy="18" r="9"/><path d="M8 44c0-10 7-15 16-15s16 5 16 15zM31 10a9 9 0 0 1 4 16c7 2 11 7 11 14"/></svg></div><div class="label">Entry Level Comp..</div></div>
    <div class="tile t-blush"><div class="ico"><svg viewBox="0 0 54 54"><rect x="4" y="11" width="46" height="33"/><path d="M4 20h46M4 26h46M22 11v15M32 11v15M22 14c0-4 10-4 10 0"/></svg></div><div class="label">Gift Card</div></div>
    <div class="tile t-lilac"><div class="ico"><svg viewBox="0 0 54 54"><path d="M27 5l3 7 7 .5-5.5 4.5 2 7-6.5-4-6.5 4 2-7-5.5-4.5 7-.5z"/><path d="M6 30h8v18H6zM14 33h10l8 4h-12M14 45h14l18-10c-2-3-5-3-8-1l-6 3"/></svg></div><div class="label">Product 5</div></div>
    <div class="tile t-lilac"><div class="ico"><svg viewBox="0 0 54 54"><circle cx="23" cy="23" r="15"/><path d="M34 34l13 13"/></svg></div><div class="label">Test 2</div></div>
    <div class="tile t-blush"><div class="ico"><svg viewBox="0 0 54 54"><path d="M20 36c0-8-8-11-8-20a15 15 0 0 1 30 0c0 9-8 12-8 20zM20 42h14M22 48h10"/></svg></div><div class="label">Test 3</div></div>
    <div class="tile t-rose"><div class="ico"><svg viewBox="0 0 54 54"><path d="M12 5h22l9 9v35H12zM34 5v9h9M18 20h19M18 26h19M18 32h12M30 42l3 3 6-7"/></svg></div><div class="label">Fast fas</div></div>
    <div class="tile t-mint"><div class="ico"><svg viewBox="0 0 54 54"><path d="M38 16V10H10v38h28V34M20 10V6h8v4M22 40l3-10 17-17 7 7-17 17z"/></svg></div><div class="label">Test 6</div></div>
  </section>

  <div class="abs pager prev"><svg viewBox="0 0 8 10"><path d="M6 1 2 5l4 4"/></svg>Previous</div>
  <div class="abs pager next">Next<svg viewBox="0 0 8 10"><path d="M2 1l4 4-4 4"/></svg></div>

  <nav class="abs cats">
    <div class="cat-arrow"><svg viewBox="0 0 9 12"><path d="M7 1 2 6l5 5"/></svg></div>
    <div class="cat-all">List All</div>
    <div class="cat">Deals</div>
    <div class="cat cat-wide">Uncategorized</div>
    <div class="cat-fill"></div>
    <div class="cat-arrow"><svg viewBox="0 0 9 12"><path d="M2 1l5 5-5 5"/></svg></div>
  </nav>

  <section class="abs order">
    <div class="order-head">
      <div class="cust"><svg viewBox="0 0 18 18"><circle cx="9" cy="6" r="4"/><path d="M2 17v-3c0-2 3-4 7-4s7 2 7 4v3z"/></svg>Select Customer</div>
      <div class="txn">Transaction #<br>00016</div>
    </div>
    <div class="order-body">
      <div class="lines"><div class="notes"><span>+</span>Add Notes</div></div>
      <div class="side"></div>
    </div>
  </section>

  <div class="abs totals">Subtotal : $0.00 &nbsp;|&nbsp; Tax : $0.00 &nbsp;|&nbsp; Disc : $0.00 &nbsp;|<br>Total : $0.00 &nbsp;|&nbsp; Paid : $0.00</div>
  <div class="abs park-plus">+</div>
  <div class="abs park">Save &amp; Park / Layby</div>
  <div class="abs pay"><span>PAY</span><span>$0.00</span></div>

  <footer class="abs footer"><span>Copyrights © 2016, www.tillnest-demo.com. All Rights Reserved.</span><span>M1</span></footer>
  <div class="abs chat"><svg viewBox="0 0 26 24"><path d="M8 5h16v11h-4v4l-4-4H8z"/><path d="M8 9H2v10h3v3l3-3h6"/><path d="M12 9h8M12 12h8"/></svg></div>

</div>
</body>
</html>
```